IT Consulting Site Revamping for Marlune

I've put a skeleton together on my website, but realize I need some help (it's http://pilot.marlune-example.ca).
I've pulled together tidbits from other websites, but really need my site to be cleaned up, and really spruced up.
I primarily focus on the IT needs of small to medium size businesses, taking care of everything from their servers and networks down to their workstations.
I also want a page listing the vendors (and logos) that I work with including Quillsoft, Zentrix, Halvor, Brax, TL, RZO, VELK, Trevo, Gatemoor.
There should also be a simple form to get a quote that will email me.
The final design should communicate strength and reliability.
I would like this to be a fully functional website, that I can upload to Plumly Pages, with the same sort of pages that are existing on http://pilot.marlune-example.ca
Updates
Hey everyone,
Hi everyone,
Reason: Hi all,
There are some designers that would like to submit some new designs, so I'm extending the deadline.
Thanks,
Target Market(s)
Small to medium size business owners. This will primarily be males who work in the oil and gas industry.
Industry/Entity Type
Consulting
Look and feel
Each slider illustrates characteristics of the customer's brand and the style your logo design should communicate.

```html
<!DOCTYPE html>
<html lang="en">
<head>
<meta charset="utf-8">
<title>Marlune Solutions</title>
<link href="https://fonts.googleapis.com/css2?family=Fredoka:wght@500;600&family=Ubuntu:wght@300;400;500&family=PT+Sans:wght@400;700&display=swap" rel="stylesheet">
<style>
:root{
  --blue:#0a7fc4;
  --blue-light:#18a7ea;
  --blue-dark:#0b5f97;
  --ink:#3a3a3a;
  --muted:#555;
  --bg:#ececec;
  --white:#fff;
  --footer:#232323;
  --footer-deep:#1a1a1a;
  --footer-text:#bdbdbd;
}
*{box-sizing:border-box;margin:0;padding:0}
html,body{width:1044px;height:1200px;overflow:hidden;background:var(--bg)}
body{font-family:"PT Sans",sans-serif;color:var(--ink);position:relative}
.page{position:absolute;inset:0}
.abs{position:absolute}

.header{left:97px;top:0;width:851px;height:117px;background:var(--white)}
.brand{left:116px;top:22px;display:flex;align-items:center;gap:12px}
.brand-dot{width:62px;height:62px;border-radius:50%;background:var(--blue)}
.brand-name{font-family:"Ubuntu",sans-serif;font-weight:500;font-size:40px;color:var(--blue);letter-spacing:-1px}
.call{right:115px;top:27px;font-family:"Ubuntu",sans-serif;font-size:17px;color:#444}
.call b{font-weight:500;color:#555}
.call .area{color:var(--blue)}

.nav{top:85px;left:480px;display:flex;align-items:flex-start;font-family:"Ubuntu",sans-serif;font-size:13px;font-weight:500;color:#444}
.nav a{display:block;padding:8px 15px 0;height:32px;text-decoration:none;color:inherit;border-right:1px solid #ddd}
.nav a:last-child{border-right:0}
.nav a.active{background:var(--blue-light);color:var(--white);border-radius:5px 5px 0 0;border-right:0;padding:8px 8px 0;margin-right:6px}
.dropdown{left:639px;top:117px;width:186px;height:135px;background:linear-gradient(#15a9ec,#0b7dc1);border-radius:0 0 6px 6px;padding:6px 8px 0 9px;z-index:3}
.dropdown a{display:block;font-family:"Ubuntu",sans-serif;font-weight:500;font-size:11.5px;color:var(--white);text-decoration:none;padding:5px 0 4px;border-bottom:1px solid rgba(255,255,255,.25)}
.dropdown a:last-child{border-bottom:0}

.tagline{left:70px;top:117px;width:904px;height:67px;background:linear-gradient(#f3f3f3,#e2e2e2);padding:7px 0 0 29px;font-family:"Fredoka",sans-serif;font-weight:600;font-size:23px;line-height:28px;color:#474747;letter-spacing:.6px}

.hero{left:97px;top:184px;width:851px;height:296px;background:linear-gradient(100deg,#4b4a58 0%,#6b6a78 45%,#8a8c99 65%,#9fb4d6 100%)}
.hero-art{left:365px;top:0;width:486px;height:296px;background:linear-gradient(90deg,rgba(120,120,135,0) 0%,rgba(150,175,215,.45) 70%,rgba(110,150,210,.7) 100%)}
.hero-title{left:12px;top:50px;font-family:"Fredoka",sans-serif;font-weight:600;font-size:26px;color:var(--blue-light);-webkit-text-stroke:1px #fff;paint-order:stroke fill}
.hero-copy{left:15px;top:86px;width:370px;font-family:"Ubuntu",sans-serif;font-weight:300;font-size:14.3px;line-height:21px;color:#f2f2f2}
.hero-copy strong{font-weight:500;font-size:15px}
.quote-btn{left:194px;top:248px;height:33px;padding:0 16px 0 18px;border-radius:17px;background:linear-gradient(#1bb0f0,#0a78be);color:var(--white);font-family:"Fredoka",sans-serif;font-weight:600;font-size:16px;line-height:33px;border:1px solid #d0ecfb}

.slider-bar{left:97px;top:480px;width:851px;height:28px;background:linear-gradient(#fafafa,#e6e6e6)}
.dots{left:477px;top:490px;display:flex;gap:6px}
.dots span{width:15px;height:15px;border-radius:50%;background:#f4f4f4;border:1px solid #d3d3d3}
.dots span.on{background:var(--blue);border-color:#0a5f96}

.content{left:97px;top:508px;width:851px;height:484px;background:var(--white)}
.section-title{left:109px;top:530px;font-family:"Fredoka",sans-serif;font-weight:600;font-size:19.5px;color:var(--blue);letter-spacing:.3px}
.intro{left:109px;top:564px;width:556px;font-size:11.3px;line-height:17.4px;color:#444}
.intro p+p{margin-top:17.4px}
.intro-art{left:674px;top:526px;width:264px;height:177px;border-radius:60px;background:radial-gradient(ellipse at center,#eef6fc 0%,#dbeaf5 60%,#f8fbfd 100%);border:3px solid #8cc8ee}

.card{top:731px;width:263px;height:229px;background:var(--white);border:1px solid #e3e3e3;box-shadow:0 1px 3px rgba(0,0,0,.08);padding:6px 11px 0}
.card h3{font-family:"Fredoka",sans-serif;font-weight:600;font-size:19px;color:#555;height:30px;padding-left:3px;letter-spacing:.3px}
.card h3 span{color:var(--blue)}
.card-photo{height:101px;margin-bottom:6px}
.card p{font-size:10.5px;line-height:15.7px;color:#333;padding-right:6px}
.read-more{position:absolute;right:6px;bottom:9px;height:21px;padding:0 8px;border-radius:3px;background:linear-gradient(#16a3e6,#0a76bb);color:var(--white);font-family:"Ubuntu",sans-serif;font-size:10.5px;line-height:21px}

.footer{left:97px;top:992px;width:851px;height:146px;background:var(--footer)}
.footer-brand{left:135px;top:1036px;display:flex;align-items:center;gap:12px}
.footer-brand .brand-dot{width:58px;height:58px}
.divider{top:1008px;width:1px;height:90px;background:#3b3b3b}
.foot-links{left:420px;top:1009px;list-style:none;font-size:11.2px;line-height:17.4px;color:var(--footer-text)}
.foot-links li::before{content:"»";color:var(--blue-light);margin-right:7px;font-size:12px}
.social{left:573px;top:1006px;list-style:none;font-size:11.2px;color:var(--footer-text)}
.social li{display:flex;align-items:center;gap:8px;height:24.4px}
.social i{display:block;width:17px;height:17px;border-radius:3px;background:#3b6fb5}
.social li:nth-child(2) i{background:#3aa6dc}
.social li:nth-child(3) i{background:#2a6fa8}
.social li:nth-child(4) i{background:#c4302b}
.field{left:723px;width:170px;background:#333;border:1px solid #3f3f3f;border-radius:4px;color:#7a7a7a;font-size:10px;padding:5px 7px}
.submit{left:842px;top:1114px;width:51px;height:18px;border-radius:3px;background:linear-gradient(#18a5e8,#0a77bc);color:var(--white);font-size:11px;line-height:18px;text-align:center}
.copyright{left:97px;top:1138px;width:851px;height:24px;background:var(--footer-deep);color:#bbb;font-size:10px;line-height:24px;text-align:center}
</style>
</head>
<body>
<div class="page">
  <header class="header abs"></header>
  <div class="brand abs"><span class="brand-dot"></span><span class="brand-name">Marlune</span></div>
  <div class="call abs"><b>Call us:</b> <span class="area">(555)</span> 014 2290</div>

  <nav class="nav abs">
    <a href="#">Home</a>
    <a href="#">About us</a>
    <a href="#" class="active">Our Services</a>
    <a href="#">Our Products</a>
    <a href="#">Contact us</a>
  </nav>
  <div class="dropdown abs">
    <a href="#">Managed IT Services</a>
    <a href="#">Storage and Virtualization</a>
    <a href="#">Networking</a>
    <a href="#">Backup and Recovery</a>
    <a href="#">Computer Repair Service</a>
  </div>

  <div class="tagline abs">Small Business Information Technology Services<br>Easy, Affordable and Reliable.</div>

  <section class="hero abs">
    <div class="hero-art abs" role="img" aria-label="Technician sketching a network diagram of servers, firewall and client PCs on glass"></div>
    <h1 class="hero-title abs">Marlune Solutions is a computer</h1>
    <p class="hero-copy abs"><strong>Solutions provider Marlune can help your small</strong> business keep your computer network under control. We are a complete network solution provider that focuses for small businesses wide variety of local small provider that focuses for smalsolution provider that focuses for small businesses wide variety of local small provider that focuses for small businesses.</p>
    <div class="quote-btn abs">Get A Quote</div>
  </section>
  <div class="slider-bar abs"></div>
  <div class="dots abs"><span></span><span class="on"></span><span></span><span></span></div>

  <div class="content abs"></div>
  <h2 class="section-title abs">Business Information Technology Services</h2>
  <div class="intro abs">
    <p><b>Marlune Solutions is a computer solutions</b> provider and IT consulting firm that supports a wide variety of local small businesses solutions provider and IT consulting firm that supports a wide variety of local small businesses Brenhollow area primarily.</p>
    <p>Marlune Solutions is a computer solutions provider and IT consulting firm that supports a wide variety of local small businesses in the &nbsp;solutions provider and IT consulting firm that supports a wide variety of local small businesses solutions provider and IT consulting firm that supports a wide variety of local small businesses Brenhollow area primarily.</p>
  </div>
  <div class="intro-art abs" role="img" aria-label="Cloud of connected servers, laptops, desktops and phones"></div>

  <article class="card abs" style="left:110px">
    <h3><span>Managed</span> IT Services</h3>
    <div class="card-photo" role="img" aria-label="Business team standing together" style="background:linear-gradient(90deg,#d9dde2,#5b6470 45%,#c9cdd2)"></div>
    <p>Contrary to popular belief, Lorem Ipsum is not simply random text. It has roots in a piece of classical Latin literature from 45 BC, making it over 2000 years old.</p>
    <span class="read-more">read more »</span>
  </article>
  <article class="card abs" style="left:390px">
    <h3><span>Net</span>working</h3>
    <div class="card-photo" role="img" aria-label="Business handshake" style="background:linear-gradient(90deg,#6f7378,#b8bcc0 50%,#dfe1e3)"></div>
    <p>Contrary to popular belief, Lorem Ipsum is not simply random text. It has roots in a piece of classical Latin literature from 45 BC, making it over 2000 years old.</p>
    <span class="read-more">read more »</span>
  </article>
  <article class="card abs" style="left:668px">
    <h3><span>Computer</span> Repair</h3>
    <div class="card-photo" role="img" aria-label="Hands working on computer internals and cables" style="background:linear-gradient(90deg,#2b2f36,#4f79a8 50%,#c9b29b)"></div>
    <p>Contrary to popular belief, Lorem Ipsum is not simply random text. It has roots in a piece of classical Latin literature from 45 BC, making it over 2000 years old.</p>
    <span class="read-more">read more »</span>
  </article>

  <footer class="footer abs"></footer>
  <div class="footer-brand abs"><span class="brand-dot"></span><span class="brand-name">Marlune</span></div>
  <span class="divider abs" style="left:402px"></span>
  <span class="divider abs" style="left:552px"></span>
  <span class="divider abs" style="left:709px"></span>
  <ul class="foot-links abs">
    <li>Home</li><li>About Us</li><li>Our Services</li><li>Our Products</li><li>Contact us</li>
  </ul>
  <ul class="social abs">
    <li><i></i>Follow us Chatterly</li>
    <li><i></i>Follow us Chirpline</li>
    <li><i></i>Follow us Linkwork</li>
    <li><i></i>Vidora</li>
  </ul>
  <div class="field abs" style="top:1000px;height:23px">Name</div>
  <div class="field abs" style="top:1031px;height:23px">Email</div>
  <div class="field abs" style="top:1061px;height:44px">Address</div>
  <div class="submit abs">Sumbit</div>
  <div class="copyright abs">© 2012 Marlune Solutions. Inc. All rights reserved.</div>
</div>
</body>
</html>
```